Beacon Lending and Capital. We provide MOSTLY residential home mortgages in Florida AND commercial loans for investment properties throughout the United states.
I would love to emulate so of the lender sites that are available on the internet but I would like to have the site as popular as possible for SEO purposes. Clients can already click the link to take them to the mortgage application where they can complete that and upload documents. If you could polish that up for me that would be great. I can also provide you with great detail on loan programs that are currently being offered. WE OFFER ALL MORTGAGE LENDING PRODUCTS. I would also like to add something in reference to the rate but I don't think it's legal to actually state or promise a rate for mortgage since they vary based on loan type, client and other criteria...

On the Beacon real estate site I would like to add a link or some way for clients to be able to put in credit card information to render services ...

Please let me know what you need from me

Thank you !!

Current link to site to improve and code

https://beaconlendingandcapital.example/

Industry/Entity Type

Residential and commmercial lending

Coding

Coded - Design and coding required

Number of Pages Required

2 page

Requirements
Must have
• Love to integrate Mortgage interest rates even if general
Nice to have
• Link to fill out mortgage application via Quillo MLO software

```html
<!DOCTYPE html>
<html lang="en">
<head>
<meta charset="utf-8">
<title>Beacon Lending and Capital</title>
<link href="https://fonts.googleapis.com/css2?family=Poppins:wght@300;400;500;600;700;800&family=Montserrat:wght@400;700;800&family=Cormorant+Garamond:wght@500&display=swap" rel="stylesheet">
<style>
:root{
  --green-dark:#1f3d1c;
  --green:#8cbb3b;
  --green-mid:#2f5a26;
  --ink:#1d1d1d;
  --text:#444;
  --muted:#8a8a8a;
  --line:#dcdcdc;
  --white:#fff;
  --orange:#f08a5d;
  --navy:#1f3a6b;
}
*{margin:0;padding:0;box-sizing:border-box}
html,body{width:1200px;height:5386px;overflow:hidden}
body{position:relative;font-family:'Poppins',sans-serif;color:var(--ink);background:var(--white)}
.abs{position:absolute}
.center{left:0;width:1200px;text-align:center}
.section-title{font-family:'Montserrat',sans-serif;font-size:34px;font-weight:400;color:var(--ink);letter-spacing:.5px}
.section-title b{font-weight:800;color:var(--green-dark)}
.rule{position:absolute;height:4px;width:70px;background:var(--green);left:565px}
.btn{position:absolute;display:flex;align-items:center;justify-content:space-between;border-radius:8px;font-size:12px;font-weight:600;letter-spacing:.3px;padding:0 6px 0 18px}
.btn .arrow{width:34px;height:34px;border-radius:6px;display:flex;align-items:center;justify-content:center}
.btn-dark{background:var(--green-dark);color:#fff}
.btn-dark .arrow{background:var(--green)}
.btn-light{background:#fff;color:var(--ink);border:1.5px solid #cfcfcf}
.btn-light .arrow{background:var(--green)}
.ph{position:absolute}
/* header */
.site-header{position:absolute;left:0;top:0;width:1200px;height:88px;background:#fff}
.brand{position:absolute;display:flex;align-items:center;gap:12px}
.brand .dot{width:44px;height:44px;border-radius:50%;background:var(--green-dark)}
.brand .name{font-family:'Poppins',sans-serif;font-weight:700;font-size:15px;color:var(--green-dark);white-space:nowrap}
.nav a{position:absolute;top:36px;font-size:12px;font-weight:500;color:var(--ink);text-decoration:none}
/* hero */
.hero-title{font-size:41px;font-weight:500;color:#fff;line-height:46px}
.hero-title span{color:var(--green);font-weight:800}
.hero-title b{font-weight:700}
/* about */
.about-text{font-size:12.5px;line-height:25.5px;color:var(--text)}
/* properties */
.prop{position:absolute;top:1286px;width:300px;height:403px}
.prop .num{position:absolute;left:0;width:300px;text-align:center;top:342px;font-size:13px;color:#fff}
.prop .street{position:absolute;left:0;width:300px;text-align:center;top:360px;font-size:22px;color:#fff;font-weight:500}
/* services */
.card{position:absolute;top:1967px;width:287px;height:333px;background:#fff;border-radius:6px;text-align:center;box-shadow:0 4px 18px rgba(0,0,0,.08)}
.card .icon{width:84px;height:86px;border-radius:14px;margin:30px auto 0;display:flex;align-items:center;justify-content:center}
.card h3{font-size:19px;font-weight:600;color:var(--green-dark);margin-top:32px}
.card p{font-size:12.5px;line-height:25px;color:var(--text);margin:6px 20px 0}
/* blog */
.date{font-size:9px;font-weight:600;color:var(--ink);display:flex;align-items:center;gap:6px}
.date i{width:13px;height:12px;border:1.5px solid #666;border-radius:2px;display:inline-block}
.blog-h{font-size:14px;font-weight:700;color:var(--ink);line-height:18px}
.blog-p{font-size:12px;color:var(--text);line-height:19px}
.more{font-size:11px;font-weight:700;color:var(--green);text-decoration:underline}
/* form */
.field{position:absolute;border:1.5px solid #ddd;border-radius:4px;font-size:12px;color:var(--muted);display:flex;align-items:center;padding-left:18px;gap:14px;background:#fff}
.field i{width:14px;height:14px;border:1.5px solid #bbb;border-radius:50%;display:inline-block}
/* footer */
.footer{position:absolute;left:0;top:5009px;width:1200px;height:377px;background:var(--green-dark);color:#fff}
.footer h4{position:absolute;top:78px;font-size:19px;font-weight:500}
.footer .lnk{position:absolute;font-size:13px;color:#fff}
.soc{position:absolute;display:flex;align-items:center;gap:12px;font-size:13px}
.soc i{width:26px;height:26px;border-radius:50%;border:1.5px solid #fff;display:inline-block}
</style>
</head>
<body>

<header class="site-header">
  <div class="brand" style="left:142px;top:22px">
    <span class="dot"></span>
    <span class="name">Beacon Lending and Capital</span>
  </div>
  <nav class="nav">
    <a style="left:612px">ABOUT</a>
    <a style="left:680px">PROPERTIES</a>
    <a style="left:776px">CONTACT US</a>
  </nav>
  <div class="btn btn-dark" style="left:880px;top:21px;width:178px;height:48px;border-radius:10px">CLIENTS PORTAL<span class="arrow"><svg width="16" height="16" viewBox="0 0 16 16"><path d="M3 13L13 3M6 3h7v7" stroke="#1f3d1c" stroke-width="1.8" fill="none"/></svg></span></div>
</header>

<section class="hero">
  <div class="ph" role="img" aria-label="Couple standing in front of a modern family home with trees" style="left:0;top:88px;width:1200px;height:529px;background:linear-gradient(90deg,#1e2a1e 0%,#3b4a34 35%,#8a8f84 60%,#5a6a70 85%,#2e3a48 100%)"></div>
  <h1 class="abs hero-title" style="left:140px;top:217px">Unlock Your Future<br>With Our Tailored<br><span>Mortgage</span> <b>Solutions</b></h1>
  <p class="abs" style="left:140px;top:363px;font-size:17px;color:#fff;line-height:28px">Residential Home Loans In Florida And<br>Commercial Lending In America</p>
  <div class="btn btn-light" style="left:140px;top:439px;width:195px;height:50px;border:none">GET STARTED NOW<span class="arrow"><svg width="16" height="16" viewBox="0 0 16 16"><path d="M3 13L13 3M6 3h7v7" stroke="#1f3d1c" stroke-width="1.8" fill="none"/></svg></span></div>
</section>

<section class="about">
  <div class="ph" role="img" aria-label="Real estate agent holding a tablet in front of a house" style="left:140px;top:684px;width:245px;height:430px;border-radius:150px 0 0 0;background:linear-gradient(160deg,#c9d3da,#8c9aa6 60%,#5b6b52)"></div>
  <div class="ph" role="img" aria-label="Agent holding a small house model" style="left:410px;top:684px;width:155px;height:148px;border-radius:50%;background:linear-gradient(150deg,#c8b9a2,#7d6b58)"></div>
  <div class="ph" role="img" aria-label="City office towers against a blue sky" style="left:410px;top:853px;width:155px;height:261px;border-radius:80px 80px 0 0;background:linear-gradient(180deg,#8fb6dc,#5a7fa8 55%,#3b5a46)"></div>
  <div class="abs" style="left:278px;top:1018px;width:230px;height:75px;border-radius:38px;background:#fff;display:flex;align-items:center;gap:12px;padding-left:10px">
    <span style="width:58px;height:58px;border-radius:50%;background:var(--green)"></span>
    <span><span style="font-size:30px;font-weight:700;color:var(--green-dark);line-height:30px;display:block">10+</span><span style="font-size:10px;font-weight:700;color:var(--green-dark)">YEAR OF EXPERIENCE</span></span>
  </div>
  <div class="abs" style="left:625px;top:712px;font-family:'Cormorant Garamond',serif;font-size:19px;color:var(--green);letter-spacing:1px">ABOUT</div>
  <h2 class="abs" style="left:625px;top:740px;font-family:'Montserrat',sans-serif;font-size:35px;line-height:44px;color:var(--ink);font-weight:400">BEACON LENDING<br><b style="font-weight:800;color:var(--green-dark)">AND CAPITAL</b></h2>
  <div class="abs" style="left:625px;top:833px;width:90px;height:3px;background:var(--green)"></div>
  <p class="abs about-text" style="left:625px;top:847px;width:440px">Beacon Lending Originates Residential Home loans in Florida and Commercial and business financing in all 50 States. We have over 25 years of experience in ALL types of real estate &amp; commercial lending. We are strategically partnered to help you obtain ALL necessary components of residential and commercial lending. From the RIGHT lending partners to the best practice insurance avenues &amp; commercial and residential real estate partners</p>
  <div class="btn btn-dark" style="left:625px;top:1056px;width:197px;height:48px">GET STARTED NOW<span class="arrow"><svg width="16" height="16" viewBox="0 0 16 16"><path d="M3 13L13 3M6 3h7v7" stroke="#1f3d1c" stroke-width="1.8" fill="none"/></svg></span></div>
</section>

<section class="properties">
  <h2 class="abs center section-title" style="top:1193px">AVAILABLE <b>PROPERTIES</b></h2>
  <div class="rule" style="top:1240px"></div>
  <div class="prop" style="left:0" role="img" aria-label="Modern white townhouse exterior"><div class="ph" style="inset:0;background:linear-gradient(180deg,#d8dde0,#9aa1a3 60%,#3a3a36)"></div><div class="num">12 PROPERTY</div><div class="street">Sunset Street</div></div>
  <div class="prop" style="left:300px" role="img" aria-label="Dark modern house at dusk"><div class="ph" style="inset:0;background:linear-gradient(180deg,#2f4666,#1f2630 60%,#3a3028)"></div><div class="num">34 PROPERTY</div><div class="street">Union Avenue</div></div>
  <div class="prop" style="left:600px" role="img" aria-label="White house with wooden cladding"><div class="ph" style="inset:0;background:linear-gradient(180deg,#dfe6ee,#b49a7a 65%,#4a4036)"></div><div class="num">56 PROPERTY</div><div class="street">Washington Street</div></div>
  <div class="prop" style="left:900px" role="img" aria-label="Brick and glass contemporary building"><div class="ph" style="inset:0;background:linear-gradient(180deg,#d6dadc,#9a5a42 60%,#3a3230)"></div><div class="num">78 PROPERTY</div><div class="street">Oak Boulevard</div></div>
  <div class="btn btn-dark" style="left:523px;top:1738px;width:154px;height:48px">VIEW MORE<span class="arrow"><svg width="16" height="16" viewBox="0 0 16 16"><path d="M3 13L13 3M6 3h7v7" stroke="#1f3d1c" stroke-width="1.8" fill="none"/></svg></span></div>
</section>

<section class="services">
  <div class="ph" role="img" aria-label="Coastal city skyline with bay and highway" style="left:0;top:1798px;width:1200px;height:684px;background:linear-gradient(180deg,#ffffff 0%,#dde9f1 25%,#8fb1c9 60%,#2f6a86 85%,#2a5a62 100%)"></div>
  <h2 class="abs center section-title" style="top:1874px">OUR <b>SERVICES</b></h2>
  <div class="rule" style="top:1921px"></div>
  <div class="card" style="left:142px"><div class="icon" style="background:var(--green)"><svg width="48" height="44" viewBox="0 0 48 44"><rect x="6" y="8" width="16" height="32" fill="none" stroke="#fff" stroke-width="3"/><rect x="26" y="18" width="16" height="22" fill="none" stroke="#fff" stroke-width="3"/><path d="M2 41h44" stroke="#fff" stroke-width="3"/></svg></div><h3>COMMERCIAL LOANS</h3><p>Lorem Ipsum is simply dummy text of the printing and typesetting industry. Lorem Ipsum has been</p><div class="btn btn-light" style="left:67px;top:262px;width:154px;height:50px">READ MORE<span class="arrow"><svg width="16" height="16" viewBox="0 0 16 16"><path d="M3 13L13 3M6 3h7v7" stroke="#1f3d1c" stroke-width="1.8" fill="none"/></svg></span></div></div>
  <div class="card" style="left:456px"><div class="icon" style="background:var(--green-dark)"><svg width="48" height="44" viewBox="0 0 48 44"><path d="M4 22L24 4l20 18" fill="none" stroke="#fff" stroke-width="3.5"/><path d="M10 18v22h28V18" fill="none" stroke="#fff" stroke-width="3.5"/><rect x="19" y="24" width="10" height="10" fill="#fff"/></svg></div><h3>RESIDENTIAL LOANS</h3><p>Lorem Ipsum is simply dummy text of the printing and typesetting industry. Lorem Ipsum has been</p><div class="btn btn-light" style="left:67px;top:262px;width:154px;height:50px">READ MORE<span class="arrow"><svg width="16" height="16" viewBox="0 0 16 16"><path d="M3 13L13 3M6 3h7v7" stroke="#1f3d1c" stroke-width="1.8" fill="none"/></svg></span></div></div>
  <div class="card" style="left:769px"><div class="icon" style="background:var(--green)"><svg width="48" height="44" viewBox="0 0 48 44"><path d="M4 22L24 4l20 18" fill="none" stroke="#fff" stroke-width="3.5"/><path d="M10 18v22h28V18" fill="none" stroke="#fff" stroke-width="3.5"/><text x="24" y="37" text-anchor="middle" font-family="Poppins" font-weight="700" font-size="16" fill="#fff">$</text></svg></div><h3>PROPERTY MORTGAGE</h3><p>Lorem Ipsum is simply dummy text of the printing and typesetting industry. Lorem Ipsum has been</p><div class="btn btn-light" style="left:67px;top:262px;width:154px;height:50px">READ MORE<span class="arrow"><svg width="16" height="16" viewBox="0 0 16 16"><path d="M3 13L13 3M6 3h7v7" stroke="#1f3d1c" stroke-width="1.8" fill="none"/></svg></span></div></div>
</section>

<section class="rates">
  <h2 class="abs center" style="top:2562px;font-family:'Montserrat',sans-serif;font-size:34px;font-weight:400;line-height:46px">STAY INFORMED<br><b style="font-weight:800;color:var(--green-dark)">ABOUT MORTGAGE RATES</b></h2>
  <div class="rule" style="top:2656px"></div>
  <p class="abs" style="left:300px;top:2686px;width:600px;text-align:center;font-size:12.5px;line-height:26px;color:var(--text)">Mortgage rates fluctuate based on various factors such as loan type, market conditions, and your personal financial profile. Rates may change frequently, and it's important to get the most accurate and up-to-date information for your unique situation.</p>
  <svg class="abs" style="left:330px;top:2791px;filter:drop-shadow(0 2px 10px rgba(0,0,0,.1))" width="540" height="408" viewBox="0 0 540 408">
    <rect width="540" height="408" rx="8" fill="#fff"/>
    <text x="8" y="34" font-family="Poppins" font-weight="600" font-size="16" fill="#1d1d1d">Last 90 Days of 30-Year Mortgage Rate Average</text>
    <text x="8" y="55" font-family="Poppins" font-size="10" fill="#444">Average of nationwide rates for 30-year fixed-rate new purchase loans with at least a 20% down</text>
    <text x="8" y="69" font-family="Poppins" font-size="10" fill="#444">payment and an applicant credit score of 680 to 739.</text>
    <g font-family="Poppins" font-size="10" fill="#555">
      <text x="9" y="91">7.8%</text><text x="9" y="120">7.6</text><text x="9" y="149">7.4</text><text x="9" y="179">7.2</text><text x="9" y="208">7.0</text><text x="9" y="237">6.8</text><text x="9" y="266">6.6</text><text x="9" y="295">6.4</text><text x="9" y="325">6.2</text><text x="9" y="354">6.0</text>
    </g>
    <g stroke="#eee" stroke-width="1"><line x1="50" y1="88" x2="532" y2="88"/><line x1="50" y1="117" x2="532" y2="117"/><line x1="50" y1="146" x2="532" y2="146"/><line x1="50" y1="176" x2="532" y2="176"/><line x1="50" y1="205" x2="532" y2="205"/><line x1="50" y1="234" x2="532" y2="234"/><line x1="50" y1="263" x2="532" y2="263"/><line x1="50" y1="292" x2="532" y2="292"/><line x1="50" y1="322" x2="532" y2="322"/><line x1="50" y1="351" x2="532" y2="351"/></g>
    <g font-family="Poppins" font-size="9.5" fill="#555" text-anchor="middle">
      <text x="65" y="370">2/19</text><text x="103" y="370">2/26</text><text x="141" y="370">3/4</text><text x="179" y="370">3/11</text><text x="217" y="370">3/18</text><text x="255" y="370">3/25</text><text x="293" y="370">4/1</text><text x="331" y="370">4/8</text><text x="369" y="370">4/15</text><text x="407" y="370">4/22</text><text x="445" y="370">4/29</text><text x="483" y="370">5/6</text><text x="521" y="370">5/13</text>
    </g>
    <polyline fill="none" stroke="var(--orange)" stroke-width="2.2" stroke-linejoin="round" points="57,205 69,198 81,208 93,217 105,202 117,212 129,227 141,241 153,259 165,249 177,231 189,220 201,212 213,222 225,237 237,246 249,255 261,249 273,237 285,227 297,217 309,205 321,208 333,198 345,187 357,193 369,176 381,183 393,168 405,179 417,151 429,164 441,173 453,190 465,183 477,193 489,202 501,198 513,205 525,198"/>
    <g fill="#fff" stroke="var(--navy)" stroke-width="1.5"><circle cx="69" cy="198" r="3"/><circle cx="153" cy="259" r="3"/><circle cx="201" cy="212" r="3"/><circle cx="249" cy="255" r="3"/><circle cx="417" cy="151" r="3"/><circle cx="525" cy="198" r="3"/></g>
    <g font-family="Poppins" font-size="10" font-weight="600" fill="var(--navy)" text-anchor="middle">
      <text x="75" y="167">7.05%</text><text x="75" y="179">Feb 22</text>
      <text x="170" y="281">6.63%</text><text x="170" y="293">Mar 5–10</text>
      <text x="212" y="178">6.95%</text><text x="212" y="190">Mar 16–17</text>
      <text x="265" y="276">6.66%</text><text x="265" y="288">Mar 27</text>
      <text x="421" y="119">7.37%</text><text x="421" y="131">Apr 25</text>
      <text x="499" y="224">7.05%</text><text x="499" y="236">May 13</text>
    </g>
    <rect x="466" y="386" width="54" height="2" fill="#ccc"/>
    <circle cx="453" cy="386" r="9" fill="var(--green-dark)"/>
  </svg>
  <div class="btn btn-dark" style="left:533px;top:3230px;width:134px;height:46px">SIGN UP<span class="arrow"><svg width="16" height="16" viewBox="0 0 16 16"><path d="M3 13L13 3M6 3h7v7" stroke="#1f3d1c" stroke-width="1.8" fill="none"/></svg></span></div>
</section>

<section class="testimonials">
  <div class="ph" role="img" aria-label="Smiling family in front of their new home" style="left:472px;top:3370px;width:586px;height:366px;border-radius:6px;background:linear-gradient(90deg,#1f3d1c 0%,#2c4a28 45%,#6a6248 80%,#8a7a5c 100%)"></div>
  <h2 class="abs" style="left:621px;top:3472px;font-family:'Montserrat',sans-serif;font-size:34px;font-weight:400;color:#fff;line-height:40px">WHAT OUR<br><b style="font-weight:800">CLIENTS SAYS</b></h2>
  <p class="abs" style="left:621px;top:3578px;width:410px;font-size:12px;line-height:25px;color:#fff">Lorem Ipsum Is Simply Dummy Text Of The Printing Typesetting Industry. Lorem Ipsum Has Been The Industry's Standard</p>
  <span class="abs" style="left:954px;top:3670px;width:33px;height:33px;border-radius:50%;background:#fff;display:flex;align-items:center;justify-content:center"><svg width="14" height="14" viewBox="0 0 14 14"><path d="M12 7H2M6 3L2 7l4 4" stroke="#1d1d1d" stroke-width="1.8" fill="none"/></svg></span>
  <span class="abs" style="left:998px;top:3670px;width:33px;height:33px;border-radius:50%;background:var(--green);display:flex;align-items:center;justify-content:center"><svg width="14" height="14" viewBox="0 0 14 14"><path d="M2 7h10M8 3l4 4-4 4" stroke="#fff" stroke-width="1.8" fill="none"/></svg></span>
  <div class="abs" style="left:142px;top:3414px;width:448px;height:276px;background:#fff;border-radius:6px;box-shadow:0 4px 20px rgba(0,0,0,.1)">
    <div class="abs" style="left:24px;top:27px;color:#f5b800;font-size:14px;letter-spacing:2px">★★★★★</div>
    <div class="ph" role="img" aria-label="Client portrait" style="left:23px;top:56px;width:64px;height:64px;border-radius:50%;background:linear-gradient(160deg,#b9b2a8,#5c554c)"></div>
    <div class="abs" style="left:101px;top:70px;font-size:15px;font-weight:600">Daniel Reyes</div>
    <div class="abs" style="left:101px;top:93px;font-size:12px;color:var(--green)">Marketing Manager</div>
    <div class="abs" style="left:374px;top:36px;font-family:'Montserrat',sans-serif;font-size:90px;font-weight:800;color:var(--green);line-height:90px">“</div>
    <p class="abs" style="left:24px;top:132px;width:400px;font-size:12px;line-height:25px;color:var(--text)">Lorem Ipsum Is Simply Dummy Text Of The Printintypesetting Industry. Lorem Ipsum Has Been The Industry's Standdummy Text Ever Since The 1500s, When An Unknown Printer Togalley Of Type And Scrambled It To Make A Type Specimen Book. It Has Survived Not Only Five Centuries</p>
  </div>
</section>

<section class="blog">
  <h2 class="abs center section-title" style="top:3812px">BLOG AND <b>RESOURCES</b></h2>
  <div class="rule" style="top:3858px"></div>
  <div class="ph" role="img" aria-label="Advisor meeting with a couple at a desk" style="left:142px;top:3893px;width:481px;height:278px;background:linear-gradient(135deg,#b69a78,#6f5a44 55%,#3f3a34)"></div>
  <div class="abs date" style="left:142px;top:4193px"><i></i>JAN 10, 2025</div>
  <div class="abs blog-h" style="left:142px;top:4217px;font-size:16px">How to Refinance Your Property Loan for Better Terms</div>
  <p class="abs blog-p" style="left:142px;top:4243px;width:470px">Lorem Ipsum Dolor Sit Amet, Consectetur Adipiscing Elit, Sed Do Eiusmod Tempor Incididunt Ut Labore Et Dolore Magna Aliqua. Ut Enim Ad Minim Veniam, Quis Nostrud Exercitation</p>
  <div class="abs more" style="left:142px;top:4314px">READ MORE</div>

  <div class="ph" role="img" aria-label="Agent presenting a house model" style="left:652px;top:3893px;width:159px;height:131px;background:linear-gradient(135deg,#c7cdd2,#6d7680)"></div>
  <div class="abs date" style="left:826px;top:3900px"><i></i>JAN 10, 2025</div>
  <div class="abs blog-h" style="left:826px;top:3918px;width:230px;font-size:12px;line-height:16px">Exploring the Pros and Cons of Fixed vs. Variable Interest Rates</div>
  <p class="abs blog-p" style="left:826px;top:3952px;width:230px;font-size:11px;line-height:17px">Lorem Ipsum Dolor Sit Consectetur Adipiscing Elit, Lorem Ipsum Dolor Sit</p>
  <div class="abs more" style="left:826px;top:4004px;font-size:10px">READ MORE</div>

  <div class="ph" role="img" aria-label="Couple holding the keys to a new home" style="left:652px;top:4041px;width:159px;height:131px;background:linear-gradient(135deg,#8aa0b0,#5a4a3c)"></div>
  <div class="abs date" style="left:826px;top:4048px"><i></i>JAN 10, 2025</div>
  <div class="abs blog-h" style="left:826px;top:4066px;width:230px;font-size:12px;line-height:16px">The Best Mortgage Loans for First-Time Homebuyers</div>
  <p class="abs blog-p" style="left:826px;top:4100px;width:230px;font-size:11px;line-height:17px">Lorem Ipsum Dolor Sit Consectetur Adipiscing Elit, Lorem Ipsum Dolor Sit</p>
  <div class="abs more" style="left:826px;top:4152px;font-size:10px">READ MORE</div>

  <div class="ph" role="img" aria-label="Two storey family house with lawn" style="left:652px;top:4188px;width:159px;height:131px;background:linear-gradient(180deg,#9cb6cf,#5c6a7a 55%,#4f6a34)"></div>
  <div class="abs date" style="left:826px;top:4195px"><i></i>JAN 10, 2025</div>
  <div class="abs blog-h" style="left:826px;top:4213px;width:230px;font-size:12px;line-height:16px">Understanding Property Loans: A Beginner's Guide</div>
  <p class="abs blog-p" style="left:826px;top:4247px;width:230px;font-size:11px;line-height:17px">Lorem Ipsum Dolor Sit Consectetur Adipiscing Elit, Lorem Ipsum Dolor Sit</p>
  <div class="abs more" style="left:826px;top:4299px;font-size:10px">READ MORE</div>

  <div class="btn btn-dark" style="left:531px;top:4367px;width:136px;height:46px">VIEW ALL<span class="arrow"><svg width="16" height="16" viewBox="0 0 16 16"><path d="M3 13L13 3M6 3h7v7" stroke="#1f3d1c" stroke-width="1.8" fill="none"/></svg></span></div>
</section>

<section class="contact">
  <h2 class="abs center section-title" style="top:4487px">GET IN <b>TOUCH</b></h2>
  <div class="rule" style="top:4533px"></div>
  <p class="abs center" style="top:4548px;font-size:12.5px;color:var(--text)">Please Send Me A Message For General Inquiries Or Reservations.</p>
  <div class="field" style="left:290px;top:4606px;width:302px;height:52px"><i></i>First Name</div>
  <div class="field" style="left:606px;top:4606px;width:302px;height:52px"><i></i>Last Name</div>
  <div class="field" style="left:290px;top:4675px;width:302px;height:52px"><i></i>Your Email</div>
  <div class="field" style="left:606px;top:4675px;width:302px;height:52px"><i></i>Phone</div>
  <div class="field" style="left:290px;top:4741px;width:618px;height:105px;align-items:flex-start;padding-top:18px"><i></i>Your Message</div>
  <div class="abs" style="left:290px;top:4873px;width:618px;height:52px;background:var(--green);border-radius:4px;color:var(--green-dark);font-size:13px;font-weight:600;display:flex;align-items:center;justify-content:center">SEND MESSAGE</div>
</section>

<footer class="footer">
  <div class="brand" style="left:142px;top:80px">
    <span class="dot" style="background:#fff;width:36px;height:36px"></span>
    <span class="name" style="color:#fff;font-size:13px">Beacon Lending and Capital</span>
  </div>
  <p class="abs" style="left:142px;top:140px;width:300px;font-size:12px;line-height:21px">Latest Updates, Exclusive Content, And Special Offers? Subscribe To Our Newsletter!</p>
  <div class="abs" style="left:142px;top:200px;width:258px;height:34px;border-radius:17px;background:#fff;display:flex;align-items:center;padding-left:30px;font-size:11px;color:var(--muted)">Your Email<span style="position:absolute;right:4px;top:4px;width:26px;height:26px;border-radius:50%;background:var(--green)"></span></div>
  <h4 style="left:481px">Quick Links</h4>
  <span class="lnk" style="left:482px;top:114px">Home</span>
  <span class="lnk" style="left:482px;top:142px">About Us</span>
  <span class="lnk" style="left:482px;top:170px">Properties</span>
  <span class="lnk" style="left:482px;top:198px">Contact Us</span>
  <h4 style="left:633px">Contact Details</h4>
  <svg class="abs" style="left:633px;top:114px" width="14" height="16" viewBox="0 0 14 16"><path d="M7 15s5-5 5-9A5 5 0 0 0 2 6c0 4 5 9 5 9z" fill="#fff"/><circle cx="7" cy="6" r="2" fill="#1f3d1c"/></svg>
  <span class="lnk" style="left:655px;top:112px;font-size:12px;line-height:20px">415 Harbor View Ln,<br>Bay City, FL USA</span>
  <svg class="abs" style="left:633px;top:166px" width="14" height="14" viewBox="0 0 14 14"><path d="M3 1l3 3-2 2c1 2 2 3 4 4l2-2 3 3-2 2C6 13 1 8 1 3z" fill="#fff"/></svg>
  <span class="lnk" style="left:655px;top:164px;font-size:12px;line-height:20px">Phone<br>+1 555 014 2290</span>
  <svg class="abs" style="left:633px;top:222px" width="14" height="12" viewBox="0 0 14 12"><rect x="1" y="1" width="12" height="10" fill="none" stroke="#fff" stroke-width="1.5"/><path d="M1 1l6 5 6-5" fill="none" stroke="#fff" stroke-width="1.5"/></svg>
  <span class="lnk" style="left:655px;top:218px;font-size:12px;line-height:20px">Email<br>info@beaconlendingandcapital.example</span>
  <h4 style="left:939px">Social Media</h4>
  <div class="soc" style="left:939px;top:113px"><i></i>FaceSpace</div>
  <div class="soc" style="left:939px;top:154px"><i></i>VidStream</div>
  <div class="soc" style="left:939px;top:195px"><i></i>ProNet</div>
  <div class="soc" style="left:939px;top:236px"><i></i>SnapGallery</div>
  <div class="abs" style="left:142px;top:328px;width:916px;height:1px;background:rgba(255,255,255,.3)"></div>
</footer>

</body>
</html>
```